Re-design existing website and add products for sale.

Our current website is very basic and cluttered. (emberfernwellness.com.au)We want a modern looking website that is easy to navigate. We also want to start selling essential oils and crystal products, so there needs to be a separate page for this. Also needs to be easily edited as we need to change the monthly oracle card with the description. Would like calming colours as we are all about natural healing. Alongside the services listed there should be a button to book now which asks for their name, email, phone number ect. and adds it to the cart.

• Logo is still being designed, please leave a space for the logo which will basically be a lotus flower within a mandala.

```html
<!DOCTYPE html>
<html lang="en">
<head>
<meta charset="utf-8">
<title>Emberfern Wellness – Home</title>
<link rel="stylesheet" href="https://fonts.googleapis.com/css2?family=Montserrat:wght@300;400;500;600&family=Open+Sans:wght@400;600;700&display=swap">
<style>
:root{
  --lavender:#8a85f7;
  --lavender-soft:#a7a3fb;
  --ink:#2c2c34;
  --muted:#8b8b95;
  --hero-dark:#262927;
  --hero-mid:#4d524e;
  --navy-deep:#0b0548;
  --navy:#2113a3;
  --footer-red:#b23a3c;
  --line:#e2e2ea;
  --canvas:#ededf0;
  --white:#ffffff;
}
*{box-sizing:border-box;margin:0;padding:0}
html,body{width:800px;height:1200px;overflow:hidden;background:var(--canvas)}
body{font-family:"Open Sans",Arial,sans-serif;color:var(--ink)}
h1,h2,h3{font-weight:400}
a{text-decoration:none}
.page{position:absolute;left:221px;top:10px;width:437px;height:1440px;background:var(--white);transform:scale(0.82);transform-origin:0 0;overflow:hidden}
.abs{position:absolute}
.heading{font-family:"Montserrat",Arial,sans-serif}

/* hero */
.hero{left:0;top:0;width:437px;height:250px;background:radial-gradient(ellipse at 62% 38%,var(--hero-mid),var(--hero-dark) 70%)}
.brand{left:46px;top:6px;display:flex;align-items:center;gap:5px;font-family:"Montserrat",Arial,sans-serif;font-size:9px;font-weight:500;color:var(--lavender-soft)}
.brand-dot{width:11px;height:11px;border-radius:50%;background:var(--lavender-soft)}
.nav{right:40px;top:8px;display:flex;gap:8px;align-items:center;font-size:4px;color:#d6d6da}
.nav .shop-link{color:var(--lavender-soft)}
.welcome{left:46px;top:70px;font-size:4px;color:#d8d8dc}
.hero-title{left:46px;top:76px;font-size:17px;font-weight:300;color:var(--white);letter-spacing:.3px}
.hero-sub{left:46px;top:99px;font-size:9.5px;font-weight:300;color:var(--lavender-soft)}
.btn{display:flex;align-items:center;justify-content:center;background:var(--lavender);color:var(--white);border-radius:8px;font-size:3.4px;font-weight:700;letter-spacing:.3px}
.hero-btn{left:46px;top:124px;width:64px;height:11px}

/* oracle */
.oracle{left:0;top:180px;width:320px;height:117px;background:var(--lavender)}
.oracle-card{left:42px;top:14px;width:72px;height:89px;border:2px solid #f3c85a;background:linear-gradient(160deg,#e9d27a,#9ec9a6 55%,#6fa58c)}
.oracle-title{left:128px;top:26px;font-size:7.5px;font-weight:500;color:var(--white)}
.oracle-date{left:128px;top:40px;font-size:4.5px;color:#eceaff}
.oracle-text{left:128px;top:52px;width:180px;font-size:3.6px;line-height:5.2px;color:var(--white)}
.oracle-text p+p{margin-top:4px}

/* intro */
.intro-q{left:58px;top:328px;width:128px;font-size:6.2px;line-height:9px;color:var(--ink)}
.intro-q p+p{margin-top:6px}
.intro-body{left:58px;top:428px;width:170px;font-size:3.5px;line-height:5px;color:var(--muted)}
.intro-body p+p{margin-top:4px}
.photo-room{left:207px;top:332px;width:136px;height:88px;background:linear-gradient(135deg,#d9d9d9,#8e8e8e 60%,#4a4a4a)}
.photo-bowl{left:257px;top:396px;width:135px;height:81px;background:linear-gradient(160deg,#6b4a2c,#2a1c12 70%);border:2px solid var(--white)}
.flower-white{left:370px;top:325px;width:67px;height:185px;background:radial-gradient(ellipse at 80% 45%,#ffffff,#e6e6e9 55%,#f7f7f8);border-radius:60% 0 0 60%}

/* about */
.lotus{left:8px;top:580px;width:130px;height:122px;background:radial-gradient(ellipse at 50% 55%,#f3a6c8,#e877a9 45%,rgba(255,255,255,0) 72%)}
.photo-family{left:58px;top:541px;width:139px;height:90px;border:2px solid var(--white);box-shadow:0 1px 4px rgba(0,0,0,.25);background:linear-gradient(140deg,#cfd6c9,#8c8a7d 55%,#4e4a45)}
.eyebrow{font-size:3.6px;letter-spacing:1.6px;color:var(--lavender)}
.about-eyebrow{left:208px;top:544px}
.about-title{left:208px;top:551px;font-size:6.5px;font-weight:400;color:var(--ink)}
.about-body{left:208px;top:569px;width:178px;font-size:3.4px;line-height:4.9px;color:var(--muted)}
.about-body p+p{margin-top:4px}
.about-body strong{color:var(--ink);font-weight:700}

/* services */
.services{left:0;top:705px;width:437px;height:232px;background:radial-gradient(ellipse at 50% 25%,var(--navy),var(--navy-deep) 80%)}
.services-eyebrow{left:0;top:732px;width:437px;text-align:center;color:#b9b5ff}
.services-title{left:0;top:738px;width:437px;text-align:center;font-size:6.3px;font-weight:400;color:var(--white)}
.service-list{left:0;top:770px;width:437px;list-style:none;text-align:center;font-size:4.6px;color:var(--white)}
.service-list li{height:13.4px;line-height:7px}
.service-list li span{border-bottom:.6px solid rgba(255,255,255,.35);padding-bottom:1.5px}

/* cards */
.card{top:910px;width:109px;height:320px;background:var(--white);border:1px solid var(--line)}
.card-img{position:absolute;left:5px;top:5px;width:99px;height:98px}
.card-title{position:absolute;left:5px;top:110px;font-size:4.7px;font-weight:600;color:var(--ink)}
.card-body{position:absolute;left:5px;top:120px;width:96px;font-size:3.3px;line-height:4.7px;color:var(--muted)}
.card-body p+p{margin-top:4px}
.card-body .price{color:var(--lavender)}
.card-body strong{color:var(--ink)}
.card-btn{position:absolute;left:5px;width:62px;height:10px}
.card-btn.is-low{top:304px}
.card-btn.is-high{top:203px}

/* contact */
.map{left:48px;top:1273px;width:174px;height:137px;background:linear-gradient(135deg,#f1f1f1,#e3e3e3);border:1px solid var(--line)}
.contact-title{left:234px;top:1276px;font-size:6px;font-weight:400;color:var(--ink)}
.contact-info{left:234px;top:1293px;font-size:3.6px;line-height:5.2px;color:var(--muted)}
.contact-info .accent{color:#e58aa8}
.field{left:234px;width:123px;border:1px solid #cfcfd6;font-size:3.4px;color:#a0a0a8;padding:2px 3px}
.send-btn{left:234px;top:1400px;width:123px;height:10px}
.footer{left:0;top:1427px;width:437px;height:13px;background:var(--footer-red);color:#f3dada;font-size:3.2px;display:flex;align-items:center;justify-content:center}
</style>
</head>
<body>
<main class="page">

  <section class="hero abs" role="img" aria-label="Dark moody close-up photograph of a lotus bud"></section>
  <svg class="abs" style="left:0;top:205px" width="437" height="50" viewBox="0 0 437 50" aria-hidden="true">
    <path d="M0,40 C110,30 250,44 330,30 C380,20 410,14 437,10 L437,50 L0,50Z" fill="#ffffff"/>
  </svg>

  <div class="brand abs"><span class="brand-dot"></span>Emberfern Wellness</div>
  <nav class="nav abs heading">
    <span>Home</span><span>About Us</span><span>Our Services</span><span class="shop-link">Shop</span><span>Contact Us</span>
    <svg width="5" height="5" viewBox="0 0 10 10" aria-hidden="true"><circle cx="4" cy="4" r="3" fill="none" stroke="#d6d6da" stroke-width="1.4"/><line x1="6.3" y1="6.3" x2="9" y2="9" stroke="#d6d6da" stroke-width="1.4"/></svg>
  </nav>
  <p class="welcome abs heading">Welcome to</p>
  <h1 class="hero-title abs heading">Emberfern Wellness</h1>
  <p class="hero-sub abs heading">Find Your True Self and Bring Balance to Your Life</p>
  <a class="btn hero-btn abs heading">MAKE AN APPOINTMENT</a>

  <section class="oracle abs">
    <div class="oracle-card abs" role="img" aria-label="Illustrated oracle card of the month"></div>
    <h2 class="oracle-title abs heading">Monthy Oracle Card</h2>
    <p class="oracle-date abs">February 2019</p>
    <div class="oracle-text abs">
      <p>Celebrate life and be spontaneous. Your happiness makes a difference to others, as when you experience happiness it radiates from you and touches those around you.</p>
      <p>Make sure to take time out for yourself and find ways to experience joy in every moment, even during the most mundane and boring tasks. Healing allows us to do this, so take care of your soul and bring healing to your life.</p>
    </div>
  </section>

  <section class="intro">
    <div class="intro-q abs heading">
      <p>Are you struggling through life, feeling stuck, not feeling yourself, or simply feeling drained?</p>
      <p>Need to find a way to relax and rejuvenate, a way to free up your energy to work on that which better serves you in this lifetime?</p>
    </div>
    <div class="intro-body abs">
      <p>Working together with you, I can help you achieve this, whether through spiritual healing sessions using Reiki and Seichim, through Oracle Card Readings or a combination of these. I am passionate about using my knowledge and skills to help others on their journey.</p>
      <p>Reiki and Seichim workshops are also available for those who wish to learn Reiki or Seichim for themselves.</p>
      <p>Each month a portion of proceeds from all services is donated to a different charity to help those in need.</p>
    </div>
    <div class="flower-white abs" role="img" aria-label="Soft white flower petals"></div>
    <div class="photo-room abs" role="img" aria-label="Photograph of the calm healing room"></div>
    <div class="photo-bowl abs" role="img" aria-label="Photograph of a brass singing bowl"></div>
  </section>

  <section class="about">
    <div class="lotus abs" role="img" aria-label="Pink lotus flower illustration"></div>
    <div class="photo-family abs" role="img" aria-label="Family photograph of the healer"></div>
    <p class="eyebrow about-eyebrow abs heading">ABOUT ME</p>
    <h2 class="about-title abs heading">My name is Clara Venn</h2>
    <div class="about-body abs">
      <p>I have always been drawn to all things spiritual and holistic, and my journey began as a young girl. I first studied Reiki many years ago and it changed my life.</p>
      <p>After suffering with a stress-related condition for years, I set about finding a solution to complement modern medicine, which would enable me to get through each day with calmer and stronger energy.</p>
      <p>It was not until later that I finally decided to use my training and abilities to help the wider community. After that, the path opened before me and I went on to become a Reiki and Seichim Master Teacher, sharing this beautiful healing with others.</p>
      <p><strong>Many years later, as an initiated Reiki &amp; Seichim Master Teacher, I'm here to provide you with intuitive healing to help balance your body, mind and spirit.</strong></p>
    </div>
  </section>

  <section class="services abs"></section>
  <svg class="abs" style="left:0;top:703px" width="437" height="14" viewBox="0 0 437 14" aria-hidden="true">
    <path d="M0,0 H437 V5 C330,12 230,2 130,8 C80,11 40,6 0,9Z" fill="#ffffff"/>
  </svg>
  <svg class="abs" style="left:0;top:915px" width="437" height="24" viewBox="0 0 437 24" aria-hidden="true">
    <path d="M0,14 C90,4 200,20 300,12 C360,7 400,2 437,0 L437,24 L0,24Z" fill="#ffffff"/>
  </svg>
  <p class="eyebrow services-eyebrow abs heading">SERVICES</p>
  <h2 class="services-title abs heading">Some of the services on offer include:</h2>
  <ul class="service-list abs">
    <li><span>Reiki &amp; Seichim Healings</span></li>
    <li><span>Energy Healing</span></li>
    <li><span>Chakra Balancing</span></li>
    <li><span>Energy Balancing</span></li>
    <li><span>Past Life Clearing</span></li>
    <li><span>Oracle Card Readings/Online Readings</span></li>
    <li><span>Distant Healing</span></li>
    <li><span>Reiki &amp; Seichim Workshops</span></li>
    <li><span>Crystals &amp; Hand Made Jewellery Available</span></li>
    <li><span>Essential Oil Roll On Blends Available</span></li>
  </ul>

  <article class="card abs" style="left:48px">
    <div class="card-img" role="img" aria-label="Violet illustration of a meditating figure" style="background:linear-gradient(160deg,#f2a7e0,#b45bc8 50%,#6a2a8e)"></div>
    <h3 class="card-title">Reiki/Seichim Healings</h3>
    <div class="card-body">
      <p class="price">1 Hour - $75<br>1/2 Hour - $40</p>
      <p><strong>Reiki</strong> is a Japanese, wonderful holistic healing technique which can help balance your energy levels, strengthen your immune system, help you relax and let go of stress and tension, and help to maintain your overall health and wellbeing. It can help clear blockages and clear your body, and is a great way to care for your whole being, cleansing the body and revealing deeper insights and messages.</p>
      <p><strong>Seichim</strong> is an ancient and powerful healing modality. It is an advanced form of healing which involves the use of sacred geometric symbols and helps clear blockages, bringing balance to body and mind. It helps clear your aura on a different level and brings peace and calm to your energy field. It is a form of healing which has been taught in many mystery schools in ancient times. Seichim is said to be the purest energy of all hands-on healing systems and is believed to have originated long ago, carried forward through generations of healers.</p>
    </div>
    <a class="btn card-btn is-low heading">BOOK NOW</a>
  </article>

  <article class="card abs" style="left:164px">
    <div class="card-img" role="img" aria-label="Illustration of glowing healing hands" style="background:radial-gradient(ellipse at 50% 45%,#f7e6b0,#d05aa0 40%,#3a2a7a 75%)"></div>
    <h3 class="card-title">Reiki &amp; Seichim Workshops</h3>
    <div class="card-body">
      <p class="price">Reiki 1 Workshop - $180<br>Reiki 2 Workshop - $280<br>Seichim Workshop - $480</p>
      <p>Reiki: A Japanese term for universal life force energy.</p>
      <p>Rei = Universal<br>Ki = Vital Energy</p>
      <p>Would you like to feel more grounded, empowered, confident and relaxed?</p>
      <p>Have you had the chance to experience Reiki or Seichim and now wish to further your knowledge of these ancient healing techniques and use them to help yourself and others around you?</p>
      <p>I offer Reiki 1 &amp; 2 workshops as well as Seichim workshops where I teach you step by step, so you can learn these wonderful techniques.</p>
      <p>Prerequisites:</p>
      <p>Reiki 1 - None</p>
      <p>Reiki 2 - Reiki 1 Certificate</p>
      <p>Seichim - Reiki 1 &amp; 2 Certificate</p>
    </div>
    <a class="btn card-btn is-low heading">BOOK NOW</a>
  </article>

  <article class="card abs" style="left:280px">
    <div class="card-img" role="img" aria-label="Blue illustrated angel oracle card deck" style="background:linear-gradient(170deg,#7fd2ef,#2f7fcf 50%,#173b86)"></div>
    <h3 class="card-title">Oracle Card Readings</h3>
    <div class="card-body">
      <p class="price">20 Min - $30</p>
      <p>Oracle cards, also known as divination cards, are used for intuition, reflection and spiritual guidance.</p>
      <p>Oracle cards offer gentle messages from a loving source, helping you to find meaningful answers to questions about your life, spiritual path and future.</p>
    </div>
    <a class="btn card-btn is-high heading">MAKE AN APPOINTMENT</a>
  </article>

  <section class="contact">
    <div class="map abs" role="img" aria-label="Street map showing the clinic location"></div>
    <h2 class="contact-title abs heading">Contact us</h2>
    <div class="contact-info abs">
      <p>12 Willow Lane<br>Seabrook SA 5999</p>
      <p style="margin-top:4px">Phone: 0400 123 456<br>E-mail: <span class="accent">hello@emberfernwellness.com.au</span></p>
    </div>
    <div class="field abs" style="top:1340px;height:11px">Name</div>
    <div class="field abs" style="top:1355px;height:11px">Email</div>
    <div class="field abs" style="top:1370px;height:26px">Message</div>
    <a class="btn send-btn abs heading">SEND</a>
  </section>

  <footer class="footer abs">Copyright 2019 © Emberfern Wellness</footer>
</main>
</body>
</html>
```